Business Card Design

Certified KFL Instructor. Self defense instruction. Ladies classes available. Semi automatic and revolver

Industry/Entity Type

Defense

```html
<!DOCTYPE html>
<html lang="en">
<head>
<meta charset="utf-8">
<title>Dana Whitfield – Business Card</title>
<link rel="stylesheet" href="https://fonts.googleapis.com/css2?family=Cardo&family=Arimo:wght@500&family=PT+Sans:wght@700&display=swap">
<style>
  :root {
    --page-bg: #ecebe7;
    --card-top: #ffffff;
    --card-bottom: #e4e6e8;
    --accent-orange: #f5971a;
    --accent-blue: #0d4596;
    --contact-blue: #163f92;
    --body-grey: #4a4d50;
  }
  html, body {
    margin: 0;
    width: 1200px;
    height: 1200px;
    overflow: hidden;
    background: var(--page-bg);
  }
  .business-card {
    position: absolute;
    left: 150px;
    top: 344px;
    width: 900px;
    height: 512px;
    background: linear-gradient(180deg, var(--card-top) 0%, #f7f8f8 45%, var(--card-bottom) 100%);
    box-shadow: 0 2px 6px rgba(0,0,0,0.18);
  }
  .card-name {
    position: absolute;
    left: 86px;
    top: 100px;
    margin: 0;
    font-family: "Cardo", serif;
    font-weight: 400;
    font-size: 52px;
    line-height: 1;
    color: var(--accent-orange);
    white-space: nowrap;
  }
  .card-contact {
    position: absolute;
    left: 86px;
    margin: 0;
    font-family: "Arimo", sans-serif;
    font-weight: 500;
    font-size: 33px;
    line-height: 1;
    color: var(--contact-blue);
    white-space: pre;
  }
  .card-contact.email { top: 163px; }
  .card-contact.phone { top: 203px; }
  .card-services {
    position: absolute;
    left: 86px;
    top: 256px;
    margin: 0;
    padding: 0;
    list-style: none;
    font-family: "PT Sans", sans-serif;
    font-weight: 700;
    font-size: 30px;
    line-height: 35px;
    letter-spacing: 0.5px;
    color: var(--body-grey);
    white-space: nowrap;
  }
  .accent-band {
    position: absolute;
    right: 0;
    top: 0;
    width: 84px;
    height: 512px;
    background: linear-gradient(180deg, var(--accent-orange) 0%, var(--accent-orange) 40%, var(--accent-blue) 65%, var(--accent-blue) 100%);
  }
</style>
</head>
<body>
  <div class="business-card">
    <h1 class="card-name">Dana Whitfield</h1>
    <p class="card-contact email">email  -  whitfieldda@postbox.net</p>
    <p class="card-contact phone">Phone  555-014-2298</p>
    <ul class="card-services">
      <li>Certified KFL Instructor</li>
      <li>Self defense instruction</li>
      <li>Ladies classes available</li>
      <li>Semi automatic and revolver</li>
    </ul>
    <div class="accent-band" role="img" aria-label="Decorative orange and blue chevron pattern along the right edge"></div>
  </div>
</body>
</html>
```